Counselling business requires poster

I require a poster to promote my counselling and coaching business I will be placing these in doctors surgery's and clinics etc.
This business is centred around helping people work through emotional issues. We provided one on one sessions which help enhance peoples lives by assisting them in overcoming their fears, obsessions, insecurities etc.

We offer support in a broad range of areas:

- Eating disorders & weight managment
- Depression
- Marriage and relationship issues
- Anxiety
- Victims of physical, verbal and/or social abuse

We want our poster to be representative of the positive, warm and welcoming atmosphere we provide.

Our motto, 'One step at a time', is symbolic of our approach and how we help our clients to tackle their problems bit by bit.

The flyer I have uploaded is just some information on what we offer

Thankyou for your designs I am taking them into consideration and will inform you of any decision.

Weight

```html
<!DOCTYPE html>
<html lang="en">
<head>
<meta charset="utf-8">
<title>Pathways Counseling – One Step at a Time</title>
<link rel="stylesheet" href="https://fonts.googleapis.com/css2?family=Antonio:wght@700&family=PT+Sans:wght@400;700&family=PT+Sans+Narrow:wght@700&display=swap">
<style>
  :root {
    --navy: #221c45;
    --amber: #f5a81c;
    --white: #ffffff;
    --photo-light: #f3c64a;
    --photo-mid: #c98d1c;
    --photo-dark: #5a3a0c;
  }
  * { box-sizing: border-box; margin: 0; padding: 0; }
  html, body { width: 849px; height: 1200px; overflow: hidden; }
  body { background: var(--navy); font-family: "PT Sans", sans-serif; }

  .poster { position: relative; width: 849px; height: 1200px; background: var(--navy); overflow: hidden; }

  .hero-photo {
    position: absolute; left: 0; top: 0; width: 849px; height: 573px;
    background:
      radial-gradient(ellipse 420px 260px at 330px 330px, rgba(255,232,140,0.85), rgba(255,232,140,0) 70%),
      linear-gradient(90deg, var(--photo-mid) 0%, var(--photo-light) 35%, var(--photo-mid) 65%, var(--photo-dark) 100%);
  }
  .hero-photo::after {
    content: ""; position: absolute; inset: 0;
    background: linear-gradient(180deg, rgba(90,58,12,0.15) 0%, rgba(0,0,0,0) 50%, rgba(120,70,10,0.35) 100%);
  }

  .brand-tab {
    position: absolute; left: 242px; top: 0; width: 378px; height: 92px;
    background: var(--white);
    display: flex; align-items: center; justify-content: center; gap: 10px;
  }
  .brand-tab .brand-dot { width: 30px; height: 30px; border-radius: 50%; background: var(--amber); }
  .brand-tab .brand-name {
    font-family: "PT Sans Narrow", sans-serif; font-weight: 700;
    font-size: 30px; color: var(--navy); letter-spacing: 0.5px;
  }

  .motto {
    position: absolute; left: 404px; top: 160px; width: 180px;
    font-family: "Antonio", sans-serif; font-weight: 700; color: var(--white);
    text-transform: uppercase; text-shadow: 2px 3px 4px rgba(0,0,0,0.45);
    text-align: center;
  }
  .motto .line-big { display: block; font-size: 152px; line-height: 128px; letter-spacing: -2px; }
  .motto .line-small { display: block; font-size: 80px; line-height: 76px; margin-top: 20px; letter-spacing: -1px; }

  .info { position: absolute; left: 248px; top: 626px; width: 370px; color: var(--amber); }
  .info h2 { font-size: 21px; font-weight: 700; margin-bottom: 48px; }
  .info p { font-size: 14px; line-height: 17px; margin-bottom: 17px; }
  .info ul { list-style: none; font-size: 14px; line-height: 17px; margin-bottom: 17px; }
  .info ul li::before { content: "- "; }

  .contact-tab {
    position: absolute; left: 242px; top: 1090px; width: 378px; height: 110px;
    background: var(--white); text-align: center; color: var(--navy);
    font-family: "PT Sans Narrow", sans-serif; font-weight: 700;
  }
  .contact-tab .contact-name { font-size: 24px; margin-top: 24px; letter-spacing: 0.5px; }
  .contact-tab .contact-line { font-size: 12px; line-height: 16px; margin-top: 4px; }
  .contact-tab .contact-line span + span { margin-left: 26px; }
</style>
</head>
<body>
<main class="poster">
  <div class="hero-photo" role="img" aria-label="Photograph of a person walking a small dog along a sunlit path through an autumn forest"></div>

  <header class="brand-tab">
    <span class="brand-dot"></span>
    <span class="brand-name">PATHWAYS COUNSELING</span>
  </header>

  <h1 class="motto">
    <span class="line-big">One</span>
    <span class="line-big">Step</span>
    <span class="line-small">At a Time</span>
  </h1>

  <section class="info">
    <h2>Professional and confidential service</h2>
    <p>Lorem ipsum dolor sit amet, consectetur adipiscing elit. Vivamus eleifend consectetur mi, quis consequat tellus euismod sit amet.</p>
    <p>Proin ac quam in urna consectetur feugiat. Nullam vulputate lobortis lacus, a dignissim nisi consequat nec.</p>
    <p>We offer support in a broad range of areas:</p>
    <ul>
      <li>Eating disorders &amp; weight managment</li>
      <li>Depression</li>
      <li>Marriage and relationship issues</li>
      <li>Anxiety</li>
    </ul>
    <p>Sed sollicitudin pellentesque magna, a pulvinar ipsum eleifend vel. Duis porta sem eget nunc pretium tincidunt. Class aptent taciti sociosqu ad litora torquent per conubia nostra, per inceptos himenaeos. Duis tempor ante non laoreet sodales. Nunc euismod lorem massa. Sed at sapien non arcu tristique ultrices id at elit.</p>
  </section>

  <footer class="contact-tab">
    <div class="contact-name">PATHWAYS COUNSELING</div>
    <div class="contact-line">58 Maple Grove Road, Riverton, Oregon 97301</div>
    <div class="contact-line"><span>Phone: (555) 210.4386</span><span>www.pathwayscounseling.com</span></div>
  </footer>
</main>
</body>
</html>
```